MALCOLM'S FIRST BIRTHDAY save the date flyer

need a digital flyer/ save the date/ so my client can text and email guests. this is not an invitation just a save the date.
This is going to be text and emaild to guests to save the date prior to the invite being sent.The feel should be fancy but not too childih looking for some excitmet, we are theying to make the theme.."love at first sight" be prdominante.

Target Market(s)

guests coming to this party

Font styles to use
Decorative

Colors

Designer to choose colors to be used in the design.

Requirements
Must have
• This is the 1st birthday, but more of an adult party. The theme is Love at first sight, we are thinking of making it like the title of a movie, but not impressing too much on it since we will reserve that part for the invitation,
Nice to have
• exciting build up
• the Childs name is Malcolm
• its a first birthday !1)
• it should have the date January 26th, 2019
• and should say Brooklyn NY
Should not have
• nothing too childish/ no cartoons or animated

```html
<!DOCTYPE html>
<html lang="en">
<head>
<meta charset="utf-8">
<title>Malcolm's First Birthday – Save the Date</title>
<link rel="stylesheet" href="https://fonts.googleapis.com/css2?family=Kaushan+Script&family=Jost:wght@500;600;700&display=swap">
<style>
  :root {
    --sky-top: #8fc3c4;
    --sky-mid: #c9e0cc;
    --sky-glow: #eeefc6;
    --sea-top: #a9e3e0;
    --sea-deep: #2f9bb2;
    --balloon-light: #f08686;
    --balloon-core: #e8464c;
    --balloon-warm: #ee7a4c;
    --ink: #0b0f14;
    --script-edge: #d9242b;
    --the-red: #7a0d10;
    --title-teal: #2a8aa6;
    --accent-red: #de2d34;
    --white: #ffffff;
  }
  * { margin: 0; padding: 0; box-sizing: border-box; }
  html, body { width: 846px; height: 1200px; overflow: hidden; background: var(--sky-top); }
  .flyer { position: relative; width: 846px; height: 1200px; overflow: hidden; }
  .backdrop {
    position: absolute; inset: 0;
    background: linear-gradient(180deg,
      var(--sky-top) 0%, var(--sky-mid) 42%, var(--sky-glow) 66%,
      #bfe2d6 76%, var(--sea-top) 79%, #6cc4cc 88%, var(--sea-deep) 100%);
  }
  .balloon-art {
    position: absolute; left: 80px; top: 70px; width: 690px; height: 790px;
    border-radius: 50%;
    background: radial-gradient(ellipse at 50% 42%,
      var(--balloon-light) 0%, var(--balloon-core) 35%, rgba(238,122,76,0.75) 58%, rgba(238,122,76,0) 72%);
  }
  .headline {
    position: absolute; left: 0; top: 0; width: 846px; height: 720px;
    font-family: "Kaushan Script", cursive;
    font-weight: 400;
    color: var(--ink);
    -webkit-text-stroke: 10px var(--script-edge);
    paint-order: stroke fill;
    line-height: 1;
  }
  .headline span { position: absolute; white-space: nowrap; }
  .headline .save {
    left: 70px; top: -10px;
    font-size: 350px; transform: rotate(-7deg); letter-spacing: -8px;
  }
  .headline .the {
    left: 385px; top: 300px;
    font-size: 110px; color: var(--the-red); -webkit-text-stroke: 0;
    transform: rotate(-7deg);
  }
  .headline .date {
    left: 195px; top: 360px;
    font-size: 340px; transform: rotate(-7deg); letter-spacing: -8px;
  }
  .tagline {
    position: absolute; left: 220px; top: 680px;
    font-family: "Kaushan Script", cursive;
    font-size: 60px; color: var(--white);
    -webkit-text-stroke: 7px var(--accent-red);
    paint-order: stroke fill;
    transform: rotate(-20deg);
    white-space: nowrap;
  }
  .details {
    position: absolute; left: 112px; top: 912px; width: 640px;
    transform: rotate(-12.5deg); transform-origin: left top;
    font-family: "Jost", sans-serif;
  }
  .rule { height: 5px; background: var(--ink); width: 640px; }
  .name {
    font-size: 104px; font-weight: 600; color: var(--title-teal);
    line-height: 1; margin-top: 8px; padding-left: 8px; letter-spacing: 1px;
    text-shadow: 5px 4px 0 var(--ink);
    white-space: nowrap;
  }
  .occasion {
    font-size: 66px; font-weight: 500; color: var(--accent-red);
    line-height: 1; margin: 4px 0 10px 50px; letter-spacing: 1px;
    white-space: nowrap;
  }
  .when-where {
    font-size: 32px; font-weight: 700; color: var(--ink);
    margin-top: 10px; padding-left: 24px; white-space: nowrap;
  }
  .when-where sup { font-size: 18px; }
</style>
</head>
<body>
<main class="flyer">
  <div class="backdrop" role="img" aria-label="Soft sky with glowing hearts above distant hills and calm sea"></div>
  <div class="balloon-art" role="img" aria-label="Heart-shaped red hot air balloon with a basket carrying a couple"></div>

  <h1 class="headline">
    <span class="save">Save</span>
    <span class="the">the</span>
    <span class="date">date</span>
  </h1>
  <p class="tagline">Love at first sight</p>

  <section class="details">
    <div class="rule"></div>
    <p class="name">MALCOLM'S</p>
    <p class="occasion">FIRST BIRTHDAY!</p>
    <div class="rule"></div>
    <p class="when-where">JANUARY 26<sup>TH</sup> 2019 | BROOKLYN NY</p>
  </section>
</main>
</body>
</html>
```